Main Banner for Hullwrap.com, SIMPLE REDESIGN

We need to redesign the main banner that appears on the homepage of our website.

Attached in the project brief is a reference.

There are alot of things we like that we want to keep from that concept but its overall just something I drew on paint and not designed well.

1. Keep yellow tabs on the right hand side, we want them bigger and bolder and to showcase the bullet points inside.
2. Get rid of the 10 yr warranty emblem and replace that with our Brandell logo also attached to the brief.
3. Keep the bottom header and include hullwrap.com and the phone number, but make it look bolder and nicer.
4. Keep the watermark

Aside from these points what we really need is this but a better cleaner more professional version of it.

Target Market(s)

Visitors to our website hullwrap.com we want this banner to include all the major selling points, branding of the product and info on how to contact us.

Requirements
Must have
• Must be clean and professional. My fear is getting submissions that are too busy or messy. There are a lot of components but the challenge is to put them all in there in a clean professional way.
Should not have
• An image in the background like a beach or some kind of picture want the focus to be the requirements listed in the project description

```html
<!DOCTYPE html>
<html lang="en">
<head>
<meta charset="UTF-8">
<title>Brandell Supreme Boat Cover – Hullwrap.com Banner</title>
<link rel="stylesheet" href="https://fonts.googleapis.com/css2?family=Archivo+Black&family=Roboto:wght@700;900&display=swap">
<style>
  :root {
    --page-bg: #014d61;
    --banner-bg-light: #fafafa;
    --banner-bg-mid: #e2e2e2;
    --watermark: rgba(140, 140, 140, 0.18);
    --title-ink: #2a2a2a;
    --accent: #ffa800;
    --accent-dark: #f39c00;
    --ink: #111111;
    --star-light: #f6cf5a;
    --star-dark: #d69a1e;
    --photo-blue: #5a67ad;
    --photo-grey: #cfcfcf;
    --logo-bg: #3a3a3a;
  }
  * { box-sizing: border-box; margin: 0; padding: 0; }
  html, body {
    width: 1200px; height: 1200px; overflow: hidden;
    background: var(--page-bg);
  }
  .banner {
    position: absolute; left: 228px; top: 430px;
    width: 746px; height: 342px; overflow: hidden;
    background: radial-gradient(ellipse at 40% 45%, var(--banner-bg-light) 0%, var(--banner-bg-mid) 100%);
  }
  .watermark {
    position: absolute; left: 336px; top: -70px;
    width: 408px; height: 408px; border-radius: 50%;
    background: var(--watermark);
  }
  .title {
    position: absolute; left: 0; right: 0; top: 14px; text-align: center;
    font-family: "Archivo Black", sans-serif; font-size: 35px; font-weight: 400;
    color: var(--title-ink); letter-spacing: 0.5px;
    text-shadow: 0 3px 4px rgba(0,0,0,0.35);
  }
  .rating {
    position: absolute; left: 236px; top: 62px;
    display: flex; gap: 11px;
  }
  .rating svg { width: 39px; height: 39px; }
  .product-photo {
    position: absolute; left: 142px; top: 112px; width: 372px; height: 188px;
    border-radius: 10px;
    background: linear-gradient(180deg, var(--photo-blue) 0%, #8b93c4 45%, var(--photo-grey) 70%, rgba(220,220,220,0.4) 100%);
  }
  .brand-mark {
    position: absolute; left: 30px; top: 82px; width: 100px; height: 124px;
    display: flex; flex-direction: column; align-items: center; justify-content: center; gap: 8px;
    background: var(--logo-bg); border-radius: 6px;
  }
  .brand-mark .dot { width: 18px; height: 18px; background: var(--accent); }
  .brand-mark .name {
    font-family: "Roboto", sans-serif; font-weight: 900; font-size: 18px; color: #ffffff;
  }
  .feature-tabs { list-style: none; }
  .feature-tab {
    position: absolute; right: 0; height: 36px;
    display: flex; align-items: center; justify-content: center;
    padding-left: 18px;
    background: linear-gradient(180deg, var(--accent) 0%, var(--accent-dark) 100%);
    clip-path: polygon(0 0, 100% 0, 100% 100%, 18px 100%);
    font-family: "Roboto", sans-serif; font-weight: 900; font-size: 17px;
    color: var(--ink); letter-spacing: 0.4px;
  }
  .feature-tab:nth-child(1) { top: 114px; left: 504px; }
  .feature-tab:nth-child(2) { top: 163px; left: 528px; }
  .feature-tab:nth-child(3) { top: 211px; left: 554px; }
  .contact-bar {
    position: absolute; left: 0; right: 0; bottom: 0; height: 36px;
    background: var(--accent);
    display: flex; align-items: center; justify-content: space-between;
    padding: 0 16px 0 20px;
    font-family: "Roboto", sans-serif; font-weight: 900; font-size: 17px; color: var(--ink);
  }
  .contact-phone { display: flex; align-items: center; gap: 9px; }
  .contact-phone svg { width: 25px; height: 25px; }
</style>
</head>
<body>
  <section class="banner">
    <div class="watermark" aria-hidden="true"></div>
    <h1 class="title">BRANDELL SUPREME BOAT COVER</h1>

    <div class="rating" aria-label="Five star rating">
      <svg viewBox="0 0 40 40"><defs><linearGradient id="starFill" x1="0" y1="0" x2="0" y2="1"><stop offset="0" stop-color="#f6cf5a"/><stop offset="1" stop-color="#d69a1e"/></linearGradient></defs><polygon points="20,2 25,14.5 38.5,15.5 28,24.2 31.3,37.5 20,30.2 8.7,37.5 12,24.2 1.5,15.5 15,14.5" fill="url(#starFill)"/></svg>
      <svg viewBox="0 0 40 40"><polygon points="20,2 25,14.5 38.5,15.5 28,24.2 31.3,37.5 20,30.2 8.7,37.5 12,24.2 1.5,15.5 15,14.5" fill="url(#starFill)"/></svg>
      <svg viewBox="0 0 40 40"><polygon points="20,2 25,14.5 38.5,15.5 28,24.2 31.3,37.5 20,30.2 8.7,37.5 12,24.2 1.5,15.5 15,14.5" fill="url(#starFill)"/></svg>
      <svg viewBox="0 0 40 40"><polygon points="20,2 25,14.5 38.5,15.5 28,24.2 31.3,37.5 20,30.2 8.7,37.5 12,24.2 1.5,15.5 15,14.5" fill="url(#starFill)"/></svg>
      <svg viewBox="0 0 40 40"><polygon points="20,2 25,14.5 38.5,15.5 28,24.2 31.3,37.5 20,30.2 8.7,37.5 12,24.2 1.5,15.5 15,14.5" fill="url(#starFill)"/></svg>
    </div>

    <div class="product-photo" role="img" aria-label="Product photo: boat on a trailer fitted with a blue strapped boat cover"></div>

    <div class="brand-mark">
      <span class="dot"></span>
      <span class="name">Brandell</span>
    </div>

    <ul class="feature-tabs">
      <li class="feature-tab">10 YR WARRANTY</li>
      <li class="feature-tab">FREE SHIPPING</li>
      <li class="feature-tab">WATERPROOF</li>
    </ul>

    <footer class="contact-bar">
      <span class="contact-site">WWW.HULLWRAP.COM</span>
      <span class="contact-phone">
        <svg viewBox="0 0 24 24" aria-hidden="true"><circle cx="12" cy="12" r="10.5" fill="none" stroke="#111111" stroke-width="2"/><path d="M8.6 6.8l1.8-.4 1 2.6-1.2 1c.6 1.3 1.5 2.2 2.8 2.8l1-1.2 2.6 1-.4 1.8c-.2.7-.8 1-1.5 1C10.9 15.2 8.8 13.1 7.6 8.3c0-.7.3-1.3 1-1.5z" fill="#111111"/></svg>
        CALL US 800 - 555 - 0142
      </span>
    </footer>
  </section>
</body>
</html>
```